Website for new dental office

I am Dr. Colin Marsh and am building a new dental practice. I specialize in general dentistry. I am young and have a higher end dental practice incorporating very new technologies and would like my website to reflect that. As many dental patients are older, the website must be very easy to navigate. I would like patients to be able to request appointments, and will eventually add on patient information forms (the health history, etc, that you normally fill out in the practice) from my practice management software, so leave an area for that.

Industry/Entity Type

Building

```html
<!DOCTYPE html>
<html lang="en">
<head>
<meta charset="utf-8">
<title>Marsh Dental – Colin Marsh, DDS</title>
<link rel="stylesheet" href="https://fonts.googleapis.com/css2?family=PT+Sans:wght@400;700&display=swap">
<style>
  :root {
    --brand: #4468b4;
    --brand-light: #6aaaf0;
    --accent: #5ba4ec;
    --ink: #222;
    --muted: #888;
    --line: #cfcfcf;
    --nav-text: #666;
    --panel: rgba(60,60,60,.88);
    --white: #fff;
  }
  * { box-sizing: border-box; margin: 0; padding: 0; }
  html, body { width: 1042px; height: 1200px; overflow: hidden; background: var(--white); }
  body { font-family: "PT Sans", Tahoma, sans-serif; color: var(--ink); position: relative; }
  a { color: inherit; text-decoration: none; }

  .site-header { position: absolute; left: 0; top: 0; width: 100%; height: 107px; }
  .brand-name { position: absolute; left: 129px; top: 10px; font-size: 47px; line-height: 1; color: var(--ink); letter-spacing: -0.5px; }
  .brand-name .first { color: var(--brand); }
  .brand-owner { position: absolute; left: 130px; top: 64px; font-size: 14px; }
  .header-phone { position: absolute; right: 130px; top: 14px; font-size: 20px; color: var(--brand-light); display: flex; align-items: center; gap: 6px; }
  .btn { display: flex; align-items: center; justify-content: center; border-radius: 20px; color: var(--white); background: var(--brand); }
  .header-cta { position: absolute; left: 610px; top: 52px; width: 302px; height: 38px; font-size: 20px; }

  .main-nav { position: absolute; left: 0; top: 107px; width: 100%; height: 34px; border-top: 1px solid var(--line); border-bottom: 1px solid var(--line); }
  .main-nav ul { list-style: none; position: absolute; left: 130px; width: 782px; top: 0; height: 100%; display: flex; justify-content: space-between; align-items: center; font-size: 11.5px; color: var(--nav-text); }
  .main-nav li { padding: 0 12px; position: relative; height: 100%; display: flex; align-items: center; }
  .main-nav li.current::before { content: ""; position: absolute; left: 1px; right: 0; top: -1px; height: 4px; background: var(--brand-light); }
  .main-nav .menu-mark { font-size: 10px; margin-left: 3px; }

  .hero { position: absolute; left: 0; top: 141px; width: 100%; height: 442px; background: linear-gradient(160deg, #d9dcd6 0%, #a9ad9d 35%, #3b4237 55%, #c9b5a7 75%, #e6d8cf 100%); }
  .hero-arrow { position: absolute; top: 212px; width: 54px; height: 54px; border-radius: 50%; background: var(--white); display: flex; align-items: center; justify-content: center; }
  .hero-arrow.prev { left: 36px; }
  .hero-arrow.next { left: 949px; }

  .appointment-form { position: absolute; left: 130px; top: 43px; width: 338px; height: 362px; background: var(--panel); padding: 23px 15px; }
  .field { display: block; width: 302px; height: 37px; border-radius: 19px; background: var(--white); color: #777; font-size: 15px; padding: 0 19px; display: flex; align-items: center; margin-bottom: 10px; }
  .field.comments { height: 107px; border-radius: 34px; align-items: flex-start; padding-top: 31px; margin-bottom: 13px; }
  .form-submit { width: 302px; height: 37px; background: var(--brand-light); font-size: 20px; }

  .procedures-title { position: absolute; left: 130px; top: 603px; width: 782px; display: flex; align-items: center; gap: 30px; color: var(--accent); font-size: 30px; }
  .procedures-title::before, .procedures-title::after { content: ""; flex: 1; height: 3px; border-top: 1px solid var(--brand-light); border-bottom: 1px solid var(--brand-light); }

  .carousel-arrow { position: absolute; top: 752px; }
  .procedure { position: absolute; top: 667px; width: 230px; text-align: center; }
  .procedure-photo { width: 193px; height: 175px; border-radius: 50%; margin: 0 auto; }
  .procedure-shadow { width: 190px; height: 10px; margin: 4px auto 0; border-radius: 50%; background: radial-gradient(ellipse, rgba(0,0,0,.15), transparent 70%); }
  .procedure h3 { font-weight: 400; font-size: 20px; margin-top: 25px; }
  .procedure .btn { width: 229px; height: 39px; margin: 20px auto 0; font-size: 15.5px; }

  .site-footer { position: absolute; left: 0; top: 1009px; width: 100%; height: 153px; border-top: 1px solid var(--line); border-bottom: 1px solid var(--line); }
  .footer-heading { font-size: 11px; color: #444; font-weight: 400; }
  .contact-info { position: absolute; left: 130px; top: 16px; }
  .contact-info p { font-size: 9.5px; color: var(--muted); line-height: 14.6px; }
  .contact-info .address { margin-top: 10px; margin-bottom: 14px; }
  .contact-info .link { color: var(--brand); }
  .location-map { position: absolute; left: 359px; top: 16px; width: 246px; height: 121px; background: linear-gradient(100deg, #a8c8f0 0%, #a8c8f0 45%, #e6e4dc 55%, #dcdcd4 100%); }
  .connect { position: absolute; left: 731px; top: 16px; }
  .social { display: flex; gap: 13px; margin-top: 11px; }
  .social span { width: 35px; height: 35px; border-radius: 50%; }
  .footer-brand { font-size: 35px; margin-top: 14px; line-height: 1; }
  .footer-brand .first { color: var(--brand); }
  .footer-owner { font-size: 9.5px; margin-top: 2px; margin-left: 6px; }
  .copyright { position: absolute; top: 1176px; width: 100%; text-align: center; font-size: 10px; color: var(--muted); }
</style>
</head>
<body>
  <header class="site-header">
    <div class="brand-name"><span class="first">Marsh</span> Dental</div>
    <div class="brand-owner">Colin Marsh, DDS</div>
    <div class="header-phone">
      <svg width="15" height="17" viewBox="0 0 15 17"><path d="M3 1 L6 5 L4.5 7 Q6 11 9 13 L11 11.5 L14 14.5 L12 16.5 Q5 15 1.5 6 Q1 3 3 1 Z" fill="var(--brand-light)"/></svg>
      555-014-2290
    </div>
    <a class="btn header-cta" href="#">Request an Appointment</a>
  </header>

  <nav class="main-nav">
    <ul>
      <li class="current">WELCOME</li>
      <li>TEAM <span class="menu-mark">&#8801;</span></li>
      <li>SERVICES <span class="menu-mark">&#8801;</span></li>
      <li>PORTFOLIO</li>
      <li>OUR OFFICE</li>
      <li>PATIENT RESOURCES <span class="menu-mark">&#8801;</span></li>
      <li>CONTACT US</li>
    </ul>
  </nav>

  <section class="hero" role="img" aria-label="Close-up photograph of a smile showing front teeth">
    <span class="hero-arrow prev"><svg width="20" height="22" viewBox="0 0 20 22"><path d="M14 2 L5 11 L14 20" fill="none" stroke="#777" stroke-width="5"/></svg></span>
    <span class="hero-arrow next"><svg width="20" height="22" viewBox="0 0 20 22"><path d="M6 2 L15 11 L6 20" fill="none" stroke="var(--brand-light)" stroke-width="5"/></svg></span>
    <form class="appointment-form">
      <span class="field">Enter your Name</span>
      <span class="field">Enter Your Phone Number</span>
      <span class="field">Enter Your Email Address</span>
      <span class="field comments">Enter Your Comments</span>
      <span class="btn form-submit">Request an Appointment</span>
    </form>
  </section>

  <h2 class="procedures-title" style="font-weight:400">OUR PROCEDURES</h2>

  <svg class="carousel-arrow" style="left:97px" width="22" height="26" viewBox="0 0 22 26"><path d="M16 2 L6 13 L16 24" fill="none" stroke="#ccc" stroke-width="4"/></svg>
  <svg class="carousel-arrow" style="left:928px" width="22" height="26" viewBox="0 0 22 26"><path d="M6 2 L16 13 L6 24" fill="none" stroke="var(--brand-light)" stroke-width="4"/></svg>

  <article class="procedure" style="left:130px">
    <div class="procedure-photo" role="img" aria-label="Photograph of a dentist placing an implant" style="background:radial-gradient(circle at 60% 45%, #e8e6e2 0%, #c9b8a8 40%, #3a2c2a 100%)"></div>
    <div class="procedure-shadow"></div>
    <h3>Dental Implants</h3>
    <a class="btn" href="#">Read More</a>
  </article>
  <article class="procedure" style="left:413px">
    <div class="procedure-photo" role="img" aria-label="Photograph of a smile with healthy teeth" style="background:radial-gradient(ellipse at 50% 50%, #5a2426 0%, #b55a55 35%, #d7968d 70%, #c78a82 100%)"></div>
    <div class="procedure-shadow"></div>
    <h3>Cosmetics</h3>
    <a class="btn" href="#">Read More</a>
  </article>
  <article class="procedure" style="left:682px">
    <div class="procedure-photo" role="img" aria-label="Photograph of a dental model for tooth replacement" style="background:linear-gradient(180deg, #d8dde6 0%, #f0e8d8 40%, #e4a898 70%, #d0d4dc 100%)"></div>
    <div class="procedure-shadow"></div>
    <h3>Tooth Replacement</h3>
    <a class="btn" href="#">Read More</a>
  </article>

  <footer class="site-footer">
    <div class="contact-info">
      <h4 class="footer-heading">CONTACT INFORMATION</h4>
      <div class="address">
        <p>Marsh Dental</p>
        <p>Street Name</p>
        <p>Location etc.</p>
      </div>
      <p>(t) 555-014-2290</p>
      <p>(e) <span class="link">hello@marshdental.example</span></p>
      <p class="link">&#8595; Download Directions</p>
    </div>
    <div class="location-map" role="img" aria-label="Map showing the office location"></div>
    <div class="connect">
      <h4 class="footer-heading">CONNECT US WITH</h4>
      <div class="social">
        <span style="background:#3b5a9a" role="img" aria-label="Social network one"></span>
        <span style="background:#5b9bd8" role="img" aria-label="Social network two"></span>
        <span style="background:#1f7cb8" role="img" aria-label="Social network three"></span>
        <span style="background:#d63a2a" role="img" aria-label="Video channel"></span>
      </div>
      <div class="footer-brand"><span class="first">Marsh</span> Dental</div>
      <div class="footer-owner">Colin Marsh, DDS</div>
    </div>
  </footer>
  <p class="copyright">Copyright &copy; 2014 Marsh Dental - Colin Marsh, DDS</p>
</body>
</html>
```